Business Cards and Logo needed for Rum Website

I need a smart, modern but fun business card (and Logo) to help promote my website BrightBarrelNotes.com

The website contains reviews of Rum (and eventually other spirits) as well as news and blog posts.

I would like a 2-sided design, with the logo and company name on one side and text on the other.

Text fields required are:
Name (Dan Fowler)
Website (www.brightbarrelnotes.com)
Email (dan@brightbarrelnotes.com)
Twitter (@BrightBarrelNotes)

For the logo i'm open to suggestions however it must incorporate a wooden Cask and a number of Stars. Ideas so far have been for a Cask surrounded in a number of Stars forming a circle around it with the text Bright Barrel Notes underneath. The logo should be modern but also a little bit cartoony and stylised. General drink/spirits themes will also be considered.

Colours: I like the idea of yellow text with black background but again i'm open to suggestions on what would work well. Contrasting colours for the 2-sides would be good.

Cards will be printed via Pelv.com so please consult their style guidelines if required: http://uk.pelv.com/help/faq/templates-and-guidelines.html

Requirements
Must have
• A spirits Cask
A number of Stars (preferrably yellow or gold)

```html
<!DOCTYPE html>
<html lang="en">
<head>
<meta charset="utf-8">
<title>Bright Barrel Notes – Business Card</title>
<link href="https://fonts.googleapis.com/css2?family=Open+Sans:wght@400;600;700&display=swap" rel="stylesheet">
<style>
  :root {
    --backdrop: #95a1a6;
    --card: #ffffff;
    --ink: #111111;
    --band-dark: #000000;
    --accent-yellow: #fde512;
    --url-yellow: #f2df1c;
    --cask-brown: #8e5a48;
  }
  * { box-sizing: border-box; margin: 0; padding: 0; }
  html, body {
    width: 1200px; height: 900px; overflow: hidden;
    background: var(--backdrop);
    font-family: "Open Sans", Arial, sans-serif;
    color: var(--ink);
  }
  .canvas { position: relative; width: 1200px; height: 900px; }
  .card {
    position: absolute; left: 320px; width: 564px; height: 370px;
    background: var(--card);
    box-shadow: 6px 7px 6px rgba(0,0,0,0.55);
    overflow: hidden;
  }
  .card--front { top: 60px; }
  .card--back { top: 468px; }

  .brand { position: absolute; display: flex; align-items: center; gap: 14px; }
  .brand__mark { border-radius: 50%; background: var(--cask-brown); flex: none; }
  .brand__name { font-weight: 700; line-height: 1.05; color: var(--ink); }

  .card--front .brand { left: 178px; top: 108px; }
  .card--front .brand__mark { width: 96px; height: 96px; }
  .card--front .brand__name { font-size: 26px; width: 110px; }

  .card--back .brand { left: 52px; top: 128px; gap: 10px; }
  .card--back .brand__mark { width: 68px; height: 68px; }
  .card--back .brand__name { font-size: 19px; width: 80px; }

  .band {
    position: absolute; left: 0; right: 0; bottom: 0;
    display: flex; align-items: center; justify-content: center;
    font-size: 20px;
  }
  .band--url { height: 54px; background: var(--band-dark); color: var(--url-yellow); }
  .band--tagline { height: 53px; background: var(--accent-yellow); color: var(--ink); }

  .contact { position: absolute; left: 271px; top: 136px; }
  .contact__name { font-size: 21px; font-weight: 700; margin-bottom: 4px; }
  .contact__line { display: flex; align-items: center; gap: 10px; font-size: 20px; line-height: 28px; }
  .contact__icon { width: 16px; height: 16px; flex: none; display: flex; align-items: center; justify-content: center; }
  .contact__dot { width: 11px; height: 11px; border-radius: 50%; background: var(--ink); }
</style>
</head>
<body>
<div class="canvas">

  <section class="card card--front">
    <div class="brand">
      <span class="brand__mark"></span>
      <span class="brand__name">Bright Barrel Notes</span>
    </div>
    <div class="band band--url">www.brightbarrelnotes.com</div>
  </section>

  <section class="card card--back">
    <div class="brand">
      <span class="brand__mark"></span>
      <span class="brand__name">Bright Barrel Notes</span>
    </div>
    <div class="contact">
      <p class="contact__name">Dan Fowler</p>
      <p class="contact__line">
        <span class="contact__icon">
          <svg width="14" height="10" viewBox="0 0 14 10" aria-hidden="true">
            <rect x="0.5" y="0.5" width="13" height="9" fill="none" stroke="#111" stroke-width="1.5"/>
            <path d="M0.5 0.5 L7 5.5 L13.5 0.5" fill="none" stroke="#111" stroke-width="1.5"/>
          </svg>
        </span>
        dan@brightbarrelnotes.com
      </p>
      <p class="contact__line">
        <span class="contact__icon"><span class="contact__dot"></span></span>
        @BrightBarrelNotes
      </p>
    </div>
    <div class="band band--tagline">rum &amp; other spirits</div>
  </section>

</div>
</body>
</html>
```